Letterhead Design Project

Standard A4 paper, center the name Sparkwell Tidy (with the mop) same as front of business card.
748 Harbourview Rd Lindenvale 5087 ABN: 71326094518
M. 0428163904 T. 83917564 Calibri font

Industry/Entity Type

Business

```html
<!DOCTYPE html>
<html lang="en">
<head>
<meta charset="utf-8">
<title>Sparkwell Tidy – Letterhead</title>
<link rel="stylesheet" href="https://fonts.googleapis.com/css2?family=Carlito:wght@400;700&display=swap">
<style>
  :root {
    --brand-dark: #1a2dbf;
    --brand-light: #6a93f4;
    --paper: #ffffff;
    --footer-text: #ffffff;
  }
  html, body {
    margin: 0;
    padding: 0;
    width: 900px;
    height: 1200px;
    overflow: hidden;
    background: var(--paper);
  }
  .letterhead {
    position: relative;
    width: 900px;
    height: 1200px;
    background: var(--paper);
    font-family: "Carlito", "Calibri", sans-serif;
    overflow: hidden;
  }
  .letterhead__waves {
    position: absolute;
    inset: 0;
    width: 900px;
    height: 1200px;
  }
  .wave--dark { fill: var(--brand-dark); }
  .wave--light { fill: var(--brand-light); }

  .brand {
    position: absolute;
    top: 108px;
    right: 70px;
    margin: 0;
  }
  .brand__name {
    font-weight: 700;
    font-size: 46px;
    line-height: 1.2;
    color: var(--brand-dark);
    letter-spacing: 0.5px;
    margin: 0;
  }

  .contact {
    position: absolute;
    left: 44px;
    top: 1030px;
    color: var(--footer-text);
    font-size: 20px;
    line-height: 33px;
    font-style: normal;
  }
  .contact__line { display: block; white-space: nowrap; }
  .contact__tel { margin-left: 34px; }
</style>
</head>
<body>
  <main class="letterhead">
    <svg class="letterhead__waves" viewBox="0 0 900 1200" aria-hidden="true">
      <path class="wave--light" d="M0 0 H760 C540 40 280 112 0 100 Z"/>
      <path class="wave--dark" d="M0 0 H650 C440 22 230 62 0 52 Z"/>
      <path class="wave--light" d="M0 935 C150 900 300 925 450 995 C600 1065 760 1105 900 1090 V1200 H0 Z"/>
      <path class="wave--dark" d="M0 978 C150 948 300 972 450 1040 C600 1105 760 1130 900 1118 V1200 H0 Z"/>
    </svg>

    <header class="brand">
      <h1 class="brand__name">Sparkwell Tidy</h1>
    </header>

    <address class="contact">
      <span class="contact__line">748 Harbourview Rd Lindenvale 5087</span>
      <span class="contact__line">Mobile: 0428163904 <span class="contact__tel">Tel: 83917564</span></span>
      <span class="contact__line">ABN: 71326094518</span>
    </address>
  </main>
</body>
</html>
```